Fast Money - Simple Book Cover Design

Hello,

I am in need of a cover for my new book. The Book Title Is

"Standing Builder - Methods for Top Rated Web Feedback That Keeps Your Calendar Full and Draws Fresh Clients Through Your Gates!"

Author: Fireman Dale Prentiss

What I want: This is a book for businesses on improving their online reputation. I want to have 5 Stars on the cover. You can look at this quarvelfind search for ideas of what I am meaning.....

(copy and paste)

http://www.quarvelfind.example/lookup?q=5+star+online+reviews&mode=pics&page=1 (copy and paste)

I am open to different color schemes for the book. I am partial to dark blues if you make it look good. Here is another book that I really like the cover of....

http://www.brindlemart.example/Clipcast-Tactics-Growing-Outreach-ebook/item/ZX93KQ7TWP

I want the cover BOLD and to STAND OUT.

I am looking for a design to help establish me as an authority for online reputation marketing. This book will be both in Pagewell format and be used in print as well.

I am open to questions....

Thanks!

Dale

Reason: I don't believe we have received the right designs. I am going to give everyone more time...

Reason: Hi everyone, I had some stuff come up and was not able to be involved in this project. I am extending because we have not seen the exact thing we want and need time to work with designers to get it right. Thanks Dale

Reason: I am currently traveling and can't wrap this up until I get back.

Target Market(s)

Business Owners

Industry/Entity Type

Business

Requirements
Must have
• Title and Subtitle

Author Name

5 Stars Images....
Nice to have
• Creativity

Bold and stand out

Professional

Should not have
• thin text, small to read text, lame graphics,

```html
<!DOCTYPE html>
<html lang="en">
<head>
<meta charset="utf-8">
<title>Standing Builder – Book Cover</title>
<link rel="stylesheet" href="https://fonts.googleapis.com/css2?family=Archivo+Black&family=Archivo:ital,wght@0,700;0,800;1,700;1,800&display=swap">
<style>
  :root {
    --navy-deep: #061a4a;
    --navy-mid: #0f2f86;
    --navy-bright: #1d4fc0;
    --band-navy: #0a2158;
    --gold-light: #fff3a0;
    --gold: #f2c230;
    --gold-deep: #c47e0c;
    --white: #ffffff;
  }
  html, body {
    margin: 0;
    padding: 0;
    width: 933px;
    height: 1200px;
    overflow: hidden;
    background: var(--navy-deep);
  }
  .cover {
    position: relative;
    width: 933px;
    height: 1200px;
    overflow: hidden;
    background:
      radial-gradient(ellipse 70% 45% at 50% 28%, var(--navy-bright) 0%, var(--navy-mid) 45%, var(--navy-deep) 100%);
  }
  .cover-rays {
    position: absolute;
    inset: 0;
  }
  .star-row {
    position: absolute;
    top: 232px;
    left: 0;
    width: 933px;
    display: flex;
    justify-content: center;
    gap: 16px;
  }
  .star-row svg {
    width: 116px;
    height: 116px;
    filter: drop-shadow(0 4px 4px rgba(0,0,0,0.45));
  }
  .title {
    position: absolute;
    top: 362px;
    left: 0;
    width: 933px;
    margin: 0;
    text-align: center;
    font-family: "Archivo Black", "Arial Black", sans-serif;
    font-size: 122px;
    line-height: 116px;
    letter-spacing: 1px;
    text-transform: uppercase;
    background: linear-gradient(180deg, var(--gold-light) 0%, var(--gold) 45%, var(--gold-deep) 100%);
    -webkit-background-clip: text;
    background-clip: text;
    color: transparent;
    filter: drop-shadow(0 5px 3px rgba(0,0,0,0.55));
  }
  .subtitle-band {
    position: absolute;
    top: 632px;
    left: 0;
    width: 933px;
    height: 272px;
    background: var(--band-navy);
    border-top: 5px solid var(--gold);
    border-bottom: 5px solid var(--gold);
    box-sizing: border-box;
    box-shadow: inset 0 10px 0 var(--navy-deep), inset 0 -10px 0 var(--navy-deep);
    text-align: center;
    color: var(--white);
  }
  .subtitle-lead {
    margin: 30px 0 0;
    font-family: "Archivo", Arial, sans-serif;
    font-weight: 800;
    font-size: 48px;
    line-height: 58px;
    text-transform: uppercase;
  }
  .subtitle-promise {
    margin: 12px 0 0;
    font-family: "Archivo", Arial, sans-serif;
    font-weight: 700;
    font-style: italic;
    font-size: 30px;
    line-height: 46px;
  }
  .author {
    position: absolute;
    top: 1022px;
    left: 0;
    width: 933px;
    text-align: center;
    font-family: "Archivo", Arial, sans-serif;
    font-weight: 800;
    color: var(--gold);
    text-transform: uppercase;
  }
  .author-label {
    position: relative;
    display: inline-block;
    font-size: 26px;
    line-height: 30px;
  }
  .author-rule {
    position: absolute;
    top: 1036px;
    left: 210px;
    width: 513px;
    height: 3px;
    background: linear-gradient(90deg, transparent 0%, var(--gold) 30%, var(--gold) 70%, transparent 100%);
  }
  .author-rule::after {
    content: "";
    position: absolute;
    left: 180px;
    width: 153px;
    top: -2px;
    height: 7px;
    background: var(--navy-deep);
  }
  .author-name {
    display: block;
    font-size: 25px;
    line-height: 30px;
  }
</style>
</head>
<body>
<main class="cover">
  <div class="cover-rays" role="img" aria-label="Sunburst rays radiating from behind the stars in deep blue tones"></div>

  <div class="star-row" aria-label="Five star rating">
    <svg viewBox="0 0 100 100" aria-hidden="true">
      <defs>
        <linearGradient id="star-gold" x1="0" y1="0" x2="0" y2="1">
          <stop offset="0" stop-color="#ffe680"/>
          <stop offset="0.5" stop-color="#e9a920"/>
          <stop offset="1" stop-color="#9a5a06"/>
        </linearGradient>
      </defs>
      <polygon points="50,3 61,37 97,37 68,58 79,93 50,72 21,93 32,58 3,37 39,37" fill="url(#star-gold)" stroke="#fff2b0" stroke-width="2"/>
    </svg>
    <svg viewBox="0 0 100 100" aria-hidden="true"><polygon points="50,3 61,37 97,37 68,58 79,93 50,72 21,93 32,58 3,37 39,37" fill="url(#star-gold)" stroke="#fff2b0" stroke-width="2"/></svg>
    <svg viewBox="0 0 100 100" aria-hidden="true"><polygon points="50,3 61,37 97,37 68,58 79,93 50,72 21,93 32,58 3,37 39,37" fill="url(#star-gold)" stroke="#fff2b0" stroke-width="2"/></svg>
    <svg viewBox="0 0 100 100" aria-hidden="true"><polygon points="50,3 61,37 97,37 68,58 79,93 50,72 21,93 32,58 3,37 39,37" fill="url(#star-gold)" stroke="#fff2b0" stroke-width="2"/></svg>
    <svg viewBox="0 0 100 100" aria-hidden="true"><polygon points="50,3 61,37 97,37 68,58 79,93 50,72 21,93 32,58 3,37 39,37" fill="url(#star-gold)" stroke="#fff2b0" stroke-width="2"/></svg>
  </div>

  <h1 class="title">Standing<br>Builder</h1>

  <section class="subtitle-band">
    <p class="subtitle-lead">“Methods for Top Rated<br>Web Feedback</p>
    <p class="subtitle-promise">That Keeps Your Calendar Full and Draws<br>Fresh Clients Through Your Gates! ”</p>
  </section>

  <div class="author-rule"></div>
  <div class="author">
    <span class="author-label">Author</span>
    <span class="author-name">Fireman Dale Prentiss</span>
  </div>
</main>
</body>
</html>
```